Information poster for parquet showroom

We are a parquet shop from germany and need some information poster for our showroom, to show our costumers some important information about parqut directly. The three posters are about reasons for parquet, and there are two types of paper on the subject. We would like to place the posters in a wooden frame. The design should be modern but simple. Enclosed I send you some of my ideas but it does not have to be like this. Can be completely different. I also send you some pictures of our showroom. 1st poster: Why parquet (dimension: 90x130 cm) Why parquet? - brings nature into your home - ecologically sustainable raw material - pleasantly warm - timeless% 26amp; high quality optics - durable% 26amp; reparable flooring - improved indoor climate - unique ride 2. Advantages oiled - tangible wood structure - natural appearance - scratches less present - partial repair possible advantage varnished - very easy-care - classic% 26amp; elegant appearance - protection against dirt and moisture - variable gloss level 3. Poster: overview of the hardness of different kinds of wood (dimension: 67x130 cm) wood hardness according to Brinell in N / mm² maple europ. 28 maple canadian. 35 birch 27 beech 33 oak 34 alder 17 ash 37 doussie 42 spruce 12 kambala 30 chestnut 18 pine 20 cherry european. 31 Larch 19 Merbau 44 Robinia 48 Sucupira 57 Elm 30 Wenge 45

```html
<!DOCTYPE html>
<html lang="de">
<head>
<meta charset="utf-8">
<title>Holzhärte nach Brinell</title>
<link rel="stylesheet" href="https://fonts.googleapis.com/css2?family=Oswald:wght@400;500;600&family=Montserrat:wght@600&display=swap">
<style>
  :root {
    --bg: #f2f2f2;
    --poster-top: #ececec;
    --panel: #d9d8da;
    --orange: #dc7c00;
    --title-orange: #e38a12;
    --band: #cc7100;
    --ink: #0d0d0d;
    --ring: #f4f4f4;
  }
  * { margin: 0; padding: 0; box-sizing: border-box; }
  html, body {
    width: 1180px;
    height: 1200px;
    overflow: hidden;
    background: var(--bg);
  }
  .poster {
    position: absolute;
    left: 304px;
    top: 29px;
    width: 572px;
    height: 1142px;
    background: var(--poster-top);
    display: flex;
    flex-direction: column;
  }
  .poster-header {
    height: 210px;
    text-align: center;
    padding-top: 56px;
  }
  .poster-title {
    font-family: "Oswald", sans-serif;
    font-weight: 600;
    font-size: 96px;
    line-height: 84px;
    letter-spacing: 7px;
    color: var(--title-orange);
    margin-left: 10px;
  }
  .poster-subtitle {
    font-family: "Montserrat", sans-serif;
    font-weight: 600;
    font-size: 31px;
    line-height: 34px;
    letter-spacing: 1px;
    color: var(--ink);
    margin-top: 2px;
  }
  .hardness-chart {
    display: block;
    background: var(--panel);
  }
  .wood-label {
    font-family: "Oswald", sans-serif;
    font-weight: 400;
    font-size: 25px;
    text-anchor: end;
  }
  .value-label {
    font-family: "Oswald", sans-serif;
    font-weight: 400;
    font-size: 19px;
    text-anchor: middle;
    fill: #ffffff;
  }
  .row-dark .wood-label { fill: var(--ink); }
  .row-dark .bar, .row-dark .marker { fill: var(--ink); }
  .row-accent .wood-label { fill: var(--orange); font-weight: 500; }
  .row-accent .bar, .row-accent .marker { fill: var(--orange); }
  .marker { stroke: var(--ring); stroke-width: 2; }
  .poster-band {
    height: 29px;
    background: var(--band);
  }
</style>
</head>
<body>
<article class="poster">
  <header class="poster-header">
    <h1 class="poster-title">HOLZHÄRTE</h1>
    <p class="poster-subtitle">nach Brinell in N/mm²</p>
  </header>

  <svg class="hardness-chart" width="572" height="903" viewBox="0 0 572 903" role="img" aria-label="Balkendiagramm der Holzhärte nach Brinell">
    <g class="row-dark" transform="translate(0,36)">
      <text class="wood-label" x="136" y="9">EICHE</text>
      <rect class="bar" x="161" y="-7.5" width="332" height="15"/>
      <circle class="marker" cx="493" cy="0" r="17"/>
      <text class="value-label" x="493" y="7">45</text>
    </g>
    <g class="row-accent" transform="translate(0,82.1)">
      <text class="wood-label" x="136" y="9">BUCHE</text>
      <rect class="bar" x="161" y="-7.5" width="323.6" height="15"/>
      <circle class="marker" cx="484.6" cy="0" r="17"/>
      <text class="value-label" x="484.6" y="7">44</text>
    </g>
    <g class="row-dark" transform="translate(0,128.2)">
      <text class="wood-label" x="136" y="9">AHORN</text>
      <rect class="bar" x="161" y="-7.5" width="306.8" height="15"/>
      <circle class="marker" cx="467.8" cy="0" r="17"/>
      <text class="value-label" x="467.8" y="7">42</text>
    </g>
    <g class="row-accent" transform="translate(0,174.3)">
      <text class="wood-label" x="136" y="9">AKAZIE</text>
      <rect class="bar" x="161" y="-7.5" width="290" height="15"/>
      <circle class="marker" cx="451" cy="0" r="17"/>
      <text class="value-label" x="451" y="7">40</text>
    </g>
    <g class="row-dark" transform="translate(0,220.4)">
      <text class="wood-label" x="136" y="9">ERLE</text>
      <rect class="bar" x="161" y="-7.5" width="273.2" height="15"/>
      <circle class="marker" cx="434.2" cy="0" r="17"/>
      <text class="value-label" x="434.2" y="7">38</text>
    </g>
    <g class="row-accent" transform="translate(0,266.5)">
      <text class="wood-label" x="136" y="9">LÄRCHE</text>
      <rect class="bar" x="161" y="-7.5" width="264.8" height="15"/>
      <circle class="marker" cx="425.8" cy="0" r="17"/>
      <text class="value-label" x="425.8" y="7">37</text>
    </g>
    <g class="row-dark" transform="translate(0,312.6)">
      <text class="wood-label" x="136" y="9">KIEFER</text>
      <rect class="bar" x="161" y="-7.5" width="248" height="15"/>
      <circle class="marker" cx="409" cy="0" r="17"/>
      <text class="value-label" x="409" y="7">35</text>
    </g>
    <g class="row-accent" transform="translate(0,358.7)">
      <text class="wood-label" x="136" y="9">KIRSCHE</text>
      <rect class="bar" x="161" y="-7.5" width="248" height="15"/>
      <circle class="marker" cx="409" cy="0" r="17"/>
      <text class="value-label" x="409" y="7">35</text>
    </g>
    <g class="row-dark" transform="translate(0,404.8)">
      <text class="wood-label" x="136" y="9">PAPPEL</text>
      <rect class="bar" x="161" y="-7.5" width="248" height="15"/>
      <circle class="marker" cx="409" cy="0" r="17"/>
      <text class="value-label" x="409" y="7">35</text>
    </g>
    <g class="row-accent" transform="translate(0,450.9)">
      <text class="wood-label" x="136" y="9">TANNE</text>
      <rect class="bar" x="161" y="-7.5" width="248" height="15"/>
      <circle class="marker" cx="409" cy="0" r="17"/>
      <text class="value-label" x="409" y="7">35</text>
    </g>
    <g class="row-dark" transform="translate(0,497)">
      <text class="wood-label" x="136" y="9">BUCHE</text>
      <rect class="bar" x="161" y="-7.5" width="231.2" height="15"/>
      <circle class="marker" cx="392.2" cy="0" r="17"/>
      <text class="value-label" x="392.2" y="7">33</text>
    </g>
    <g class="row-accent" transform="translate(0,543.1)">
      <text class="wood-label" x="136" y="9">AHORN</text>
      <rect class="bar" x="161" y="-7.5" width="214.4" height="15"/>
      <circle class="marker" cx="375.4" cy="0" r="17"/>
      <text class="value-label" x="375.4" y="7">31</text>
    </g>
    <g class="row-dark" transform="translate(0,589.2)">
      <text class="wood-label" x="136" y="9">AKAZIE</text>
      <rect class="bar" x="161" y="-7.5" width="214.4" height="15"/>
      <circle class="marker" cx="375.4" cy="0" r="17"/>
      <text class="value-label" x="375.4" y="7">31</text>
    </g>
    <g class="row-accent" transform="translate(0,635.3)">
      <text class="wood-label" x="136" y="9">ERLE</text>
      <rect class="bar" x="161" y="-7.5" width="206" height="15"/>
      <circle class="marker" cx="367" cy="0" r="17"/>
      <text class="value-label" x="367" y="7">30</text>
    </g>
    <g class="row-dark" transform="translate(0,681.4)">
      <text class="wood-label" x="136" y="9">LÄRCHE</text>
      <rect class="bar" x="161" y="-7.5" width="189.2" height="15"/>
      <circle class="marker" cx="350.2" cy="0" r="17"/>
      <text class="value-label" x="350.2" y="7">28</text>
    </g>
    <g class="row-accent" transform="translate(0,727.5)">
      <text class="wood-label" x="136" y="9">KIEFER</text>
      <rect class="bar" x="161" y="-7.5" width="172.4" height="15"/>
      <circle class="marker" cx="333.4" cy="0" r="17"/>
      <text class="value-label" x="333.4" y="7">26</text>
    </g>
    <g class="row-dark" transform="translate(0,773.6)">
      <text class="wood-label" x="136" y="9">KIRSCHE</text>
      <rect class="bar" x="161" y="-7.5" width="172.4" height="15"/>
      <circle class="marker" cx="333.4" cy="0" r="17"/>
      <text class="value-label" x="333.4" y="7">26</text>
    </g>
    <g class="row-accent" transform="translate(0,819.7)">
      <text class="wood-label" x="136" y="9">PAPPEL</text>
      <rect class="bar" x="161" y="-7.5" width="172.4" height="15"/>
      <circle class="marker" cx="333.4" cy="0" r="17"/>
      <text class="value-label" x="333.4" y="7">26</text>
    </g>
    <g class="row-dark" transform="translate(0,865.8)">
      <text class="wood-label" x="136" y="9">TANNE</text>
      <rect class="bar" x="161" y="-7.5" width="164" height="15"/>
      <circle class="marker" cx="325" cy="0" r="17"/>
      <text class="value-label" x="325" y="7">25</text>
    </g>
  </svg>

  <div class="poster-band"></div>
</article>
</body>
</html>
```